Quorvex Labworks Website

All the descriptions are available in the attached file. The designer has to structure the website and find the right images and icons. The website should look modern and avoid using images of real humans rather use animated images. Please note that the design should include home page, all the 4 services page , the contact us would be at the bottom of home page.

```html
<!DOCTYPE html>
<html lang="en">
<head>
<meta charset="utf-8">
<title>Quorvex Labworks</title>
<link rel="stylesheet" href="https://fonts.googleapis.com/css2?family=Audiowide&family=Roboto:wght@400;500&display=swap">
<style>
:root{
  --blue:#1a6fd8;
  --blue-deep:#0f56c0;
  --blue-hero-top:#2f86e6;
  --blue-hero-bottom:#4c9cf0;
  --pale:#e4eefb;
  --pale-2:#d3e3f8;
  --circle:#a9c9f2;
  --text:#4a4f58;
  --white:#ffffff;
  --footer:#5d5d5d;
  --footer-dark:#4e4e4e;
  --heading:"Audiowide",sans-serif;
  --body:"Roboto",sans-serif;
}
*{box-sizing:border-box;margin:0;padding:0}
html,body{width:1200px;height:4594px;overflow:hidden;background:var(--white)}
body{position:relative;font-family:var(--body);color:var(--text)}
.abs{position:absolute}
.deco{position:absolute;left:0;top:0;width:1200px;height:4594px}
.brand{display:flex;align-items:center;gap:12px;font-family:var(--heading);color:var(--blue);font-size:28px;line-height:32px;white-space:nowrap}
.brand-name{display:block}
.brand-mark{width:20px;height:20px;background:var(--blue);flex:none}
.nav{display:flex;gap:38px;font-family:var(--heading);font-size:18px;color:var(--blue);text-transform:uppercase;white-space:nowrap}
.hero{position:absolute;left:0;top:130px;width:1200px;height:600px}
.hero-title{position:absolute;left:46px;top:262px;font-family:var(--heading);color:var(--white);font-size:43px;line-height:62px;text-transform:uppercase;letter-spacing:1px}
.art{position:absolute;border-radius:24px}
.section-title{font-family:var(--heading);color:var(--blue);font-size:31px;text-transform:uppercase;letter-spacing:1px}
.copy{font-size:19.5px;line-height:37.7px;color:var(--text)}
.btn{position:absolute;width:226px;height:63px;background:var(--blue);color:var(--white);font-family:var(--heading);font-size:19px;display:flex;align-items:center;padding-left:28px;text-transform:uppercase;clip-path:polygon(0 0,88% 0,100% 50%,88% 100%,0 100%)}
.btn::after{content:"";position:absolute;right:0;top:0;width:30px;height:100%;background:var(--blue-deep);clip-path:polygon(0 0,40% 0,100% 50%,40% 100%,0 100%)}
.num{position:absolute;width:78px;height:78px;border-radius:50%;background:var(--circle);border:3px solid #8fb6ea;display:flex;align-items:center;justify-content:center;font-family:var(--heading);font-size:30px;color:var(--blue-deep)}
.icon{position:absolute;width:90px;height:80px}
.svc-title{position:absolute;font-family:var(--heading);color:var(--blue);font-size:29px;text-transform:uppercase;white-space:nowrap}
.contact{position:absolute;left:9px;top:3723px;width:1180px;height:547px;background:var(--white);box-shadow:0 0 10px rgba(0,0,0,.15)}
.contact-info{position:absolute;left:0;top:0;width:479px;height:547px;background:var(--blue)}
.info-row{position:absolute;left:59px;display:flex;align-items:center;gap:26px;color:var(--white);font-size:20px;line-height:38px;white-space:nowrap}
.info-ico{width:76px;height:76px;border-radius:50%;background:var(--white);display:flex;align-items:center;justify-content:center;flex:none}
.field{position:absolute;left:526px;width:513px;border-bottom:2px solid #bbb;font-size:17px;color:#555;padding:0 0 10px 8px;text-transform:uppercase}
.footer{position:absolute;left:0;top:4280px;width:1200px;height:314px;background:var(--footer)}
.footer .nav{color:var(--white);font-size:18px;gap:40px}
.social{width:36px;height:36px;border-radius:8px}
.copyright{font-family:var(--heading);color:var(--white);font-size:15px;text-transform:uppercase;white-space:nowrap}
</style>
</head>
<body>

<svg class="deco" viewBox="0 0 1200 4594" aria-hidden="true">
  <path d="M0 720 C200 700 120 1100 0 1300 Z" fill="var(--pale)"/>
  <path d="M1200 1180 C1060 1220 980 1380 1200 1560 Z" fill="var(--pale)"/>
  <path d="M0 1900 C160 1960 130 2350 0 2520 Z" fill="var(--pale)"/>
  <path d="M1200 2480 C1020 2560 990 2860 1200 3050 Z" fill="var(--pale)"/>
  <path d="M0 3080 C180 3150 160 3520 0 3700 Z" fill="var(--pale)"/>
  <path d="M1200 3120 C1100 3200 1080 3500 1200 3620 Z" fill="var(--pale)"/>
  <circle cx="232" cy="2230" r="200" fill="none" stroke="var(--pale-2)" stroke-width="3"/>
  <circle cx="840" cy="2820" r="250" fill="none" stroke="var(--pale-2)" stroke-width="3"/>
  <circle cx="300" cy="3400" r="270" fill="none" stroke="var(--pale-2)" stroke-width="3"/>
</svg>

<header>
  <div class="brand abs" style="left:116px;top:40px"><span class="brand-mark"></span><span class="brand-name">Quorvex<br>Labworks</span></div>
  <nav class="nav abs" style="left:433px;top:63px">
    <span>Home</span><span>Services</span><span>Products</span><span>Blog</span><span>Contact Us</span>
  </nav>
</header>

<section class="hero">
  <svg width="1200" height="600" viewBox="0 0 1200 600" aria-hidden="true">
    <defs>
      <linearGradient id="heroGrad" x1="0" y1="0" x2="0" y2="1">
        <stop offset="0" stop-color="var(--blue-hero-top)"/>
        <stop offset="1" stop-color="var(--blue-hero-bottom)"/>
      </linearGradient>
    </defs>
    <path d="M0 10 C400 -5 800 20 1200 0 L1200 580 C1000 560 820 520 560 540 C300 560 120 590 0 570 Z" fill="url(#heroGrad)"/>
    <path d="M0 570 C200 520 420 470 700 520 C900 555 1050 590 1200 580 L1200 600 L0 600 Z" fill="var(--white)" opacity=".35"/>
  </svg>
</section>
<h1 class="hero-title">Empower your<br>digital journey<br>with our advanced<br>IT solutions</h1>
<div class="art" role="img" aria-label="Illustration of a developer at a desk with monitors and floating technology tags" style="left:615px;top:175px;width:475px;height:485px;background:linear-gradient(160deg,#5aa6f3,#2a74d6);opacity:.85"></div>

<section class="about">
  <div class="art" role="img" aria-label="Illustration of a designer interacting with floating interface panels" style="left:20px;top:790px;width:530px;height:465px;background:linear-gradient(150deg,#c9b8f2,#7f9ef0)"></div>
  <h2 class="section-title abs" style="left:597px;top:790px">About Us</h2>
  <p class="copy abs" style="left:599px;top:856px;width:480px">We are a forward-thinking IT consulting firm specializing in providing cutting-edge data analytics, web application development, and mobile app development services. Our passion for innovation and technology drives us to deliver tailor-made solutions that empower businesses to thrive in the digital landscape. We take pride in our ability to collaborate with early-stage startups as their</p>
  <span class="btn" style="left:599px;top:1188px">Learn More</span>
</section>

<h2 class="section-title abs" style="left:0;width:1200px;text-align:center;top:1330px">Services</h2>

<section class="service">
  <div class="num" style="left:110px;top:1413px">01</div>
  <svg class="icon" style="left:240px;top:1410px" viewBox="0 0 90 80" aria-hidden="true"><rect x="4" y="4" width="64" height="50" rx="4" fill="none" stroke="var(--blue-deep)" stroke-width="3"/><rect x="16" y="30" width="6" height="16" fill="var(--blue)"/><rect x="26" y="22" width="6" height="24" fill="var(--blue)"/><rect x="36" y="28" width="6" height="18" fill="var(--blue)"/><circle cx="58" cy="52" r="14" fill="#fff" stroke="var(--blue-deep)" stroke-width="3"/><line x1="68" y1="62" x2="82" y2="76" stroke="var(--blue-deep)" stroke-width="5"/></svg>
  <h3 class="svc-title" style="left:109px;top:1520px;text-transform:none">Data Analytics</h3>
  <p class="copy abs" style="left:110px;top:1576px;width:440px">At Quorvex Labworks, our proficiency consists of linking your leadership team's objectives with the relevant data that holds significance. We recognize the importance of not only delivering precise and dependable data but also presenting it in a format that is</p>
  <span class="btn" style="left:110px;top:1828px">Read More</span>
  <div class="art" role="img" aria-label="Illustration of a team reviewing charts on large screens" style="left:567px;top:1420px;width:620px;height:445px;background:linear-gradient(160deg,#d7deea,#9aa9c4)"></div>
</section>

<section class="service">
  <div class="art" role="img" aria-label="Illustration of a web developer coding at a green desk with code tags" style="left:60px;top:1990px;width:510px;height:490px;background:linear-gradient(150deg,#7fe0cf,#1f8a78)"></div>
  <div class="num" style="left:710px;top:1987px">02</div>
  <svg class="icon" style="left:835px;top:1990px" viewBox="0 0 90 80" aria-hidden="true"><rect x="4" y="6" width="64" height="48" rx="5" fill="none" stroke="var(--blue-deep)" stroke-width="3"/><line x1="4" y1="18" x2="68" y2="18" stroke="var(--blue-deep)" stroke-width="3"/><text x="14" y="42" font-size="16" fill="var(--blue)" font-family="Roboto">&lt;/&gt;</text><circle cx="66" cy="58" r="13" fill="#fff" stroke="var(--blue-deep)" stroke-width="4" stroke-dasharray="5 3"/></svg>
  <h3 class="svc-title" style="left:711px;top:2094px">Web Development</h3>
  <p class="copy abs" style="left:711px;top:2150px;width:420px">At Quorvex Labworks, we are a trailblazing web development company committed to delivering cutting-edge digital solutions that empower businesses to excel in the ever-evolving online landscape. Our team of seasoned professionals combines</p>
  <span class="btn" style="left:710px;top:2402px">Read More</span>
</section>

<section class="service">
  <div class="num" style="left:77px;top:2588px">03</div>
  <svg class="icon" style="left:195px;top:2585px" viewBox="0 0 90 80" aria-hidden="true"><rect x="16" y="2" width="40" height="74" rx="6" fill="none" stroke="var(--blue-deep)" stroke-width="3"/><circle cx="48" cy="40" r="16" fill="#fff" stroke="var(--blue)" stroke-width="3"/><circle cx="48" cy="36" r="5" fill="var(--blue)"/><line x1="2" y1="30" x2="14" y2="30" stroke="var(--blue-deep)" stroke-width="3"/><line x1="2" y1="44" x2="14" y2="44" stroke="var(--blue-deep)" stroke-width="3"/></svg>
  <h3 class="svc-title" style="left:71px;top:2696px">Mobile App Development</h3>
  <p class="copy abs" style="left:77px;top:2752px;width:450px">At Quorvex Labworks, we are a pioneering mobile app development company dedicated to crafting exceptional digital experiences that captivate and engage users across various platforms. Our team of expert developers and designers combines passion,</p>
  <span class="btn" style="left:77px;top:3004px">Read More</span>
  <div class="art" role="img" aria-label="Illustration of a team assembling a giant phone with language blocks" style="left:640px;top:2580px;width:465px;height:490px;background:linear-gradient(160deg,#8fb3f2,#2c5fd0)"></div>
</section>

<section class="service">
  <div class="art" role="img" aria-label="Illustration of a team building a rocket among gears" style="left:90px;top:3150px;width:540px;height:488px;background:linear-gradient(160deg,#e0d6ee,#a894c8)"></div>
  <div class="num" style="left:710px;top:3161px">04</div>
  <svg class="icon" style="left:815px;top:3158px" viewBox="0 0 90 80" aria-hidden="true"><circle cx="40" cy="14" r="11" fill="none" stroke="var(--blue)" stroke-width="3"/><text x="35" y="20" font-size="15" fill="var(--blue)" font-family="Roboto">$</text><path d="M8 76 V48 L22 34 L36 48 V76" fill="none" stroke="var(--blue-deep)" stroke-width="3"/><path d="M44 76 V48 L58 34 L72 48 V76" fill="none" stroke="var(--blue-deep)" stroke-width="3"/></svg>
  <h3 class="svc-title" style="left:711px;top:3270px">Start-Up Partner</h3>
  <p class="copy abs" style="left:711px;top:3325px;width:450px">At Quorvex Labworks, we are committed to supporting early-stage start-ups on their journey to success by providing comprehensive technical partner services. Our team of industry veterans collaborates with entrepreneurs to refine their ideas, develop</p>
  <span class="btn" style="left:710px;top:3575px">Read More</span>
</section>

<section class="contact">
  <div class="contact-info">
    <div class="info-row" style="top:99px">
      <span class="info-ico"><svg width="34" height="40" viewBox="0 0 34 40" aria-hidden="true"><path d="M17 2 C8 2 2 9 2 17 C2 28 17 38 17 38 C17 38 32 28 32 17 C32 9 26 2 17 2 Z" fill="var(--blue)"/><circle cx="17" cy="16" r="6" fill="#fff"/></svg></span>
      <span>Suite 12/48 Harlowe Avenue,<br>Brenton WA 6999</span>
    </div>
    <div class="info-row" style="top:217px">
      <span class="info-ico"><svg width="32" height="32" viewBox="0 0 32 32" aria-hidden="true"><path d="M7 2 L12 2 L14 10 L10 13 C12 18 15 21 19 22 L22 18 L30 20 L30 26 C30 28 28 30 26 30 C13 29 3 19 2 6 C2 4 4 2 7 2 Z" fill="var(--blue)"/></svg></span>
      <span>+61 (08) 5550 2741<br>&nbsp;(Sales / Support)</span>
    </div>
    <div class="info-row" style="top:349px">
      <span class="info-ico"><svg width="38" height="28" viewBox="0 0 38 28" aria-hidden="true"><rect x="1" y="1" width="36" height="26" rx="3" fill="var(--blue)"/><path d="M3 4 L19 16 L35 4" fill="none" stroke="#fff" stroke-width="2.5"/></svg></span>
      <span style="font-size:18px">dev@quorvexlabworks.example</span>
    </div>
  </div>
  <h2 class="section-title abs" style="left:526px;top:50px">Contact Us</h2>
  <div class="field" style="top:138px">Name</div>
  <div class="field" style="top:212px">Email</div>
  <div class="field" style="top:290px">Phone Number</div>
  <div class="field" style="top:368px">Message</div>
  <span class="btn" style="left:522px;top:449px;padding-left:58px">Submit</span>
</section>

<footer class="footer">
  <div class="brand abs" style="left:0;width:1200px;justify-content:center;top:50px;color:var(--white)"><span class="brand-mark"></span><span class="brand-name">Quorvex<br>Labworks</span></div>
  <nav class="nav abs" style="left:0;width:1200px;justify-content:center;top:176px">
    <span>Home</span><span>Services</span><span>Products</span><span>Blog</span><span>Contact Us</span>
  </nav>
  <div class="abs" style="left:0;top:230px;width:1200px;height:2px;background:var(--footer-dark)"></div>
  <div class="abs" style="left:108px;top:258px;display:flex;gap:12px">
    <span class="social" style="background:#c2439b"></span>
    <span class="social" style="background:#3fbf5a"></span>
    <span class="social" style="background:#3a9ee8"></span>
  </div>
  <div class="abs copyright" style="right:112px;top:268px">©2023 Copyrights. Quorvex Labworks. All rights reserved.</div>
</footer>

</body>
</html>
```